Website Design for a Graphic Design Studio in California

We are working with a graphic design company in California.
PLEASE NOTE: We report and ban any designer that reaches out directly to our customers.

Some sites to use for content/competitors and inspiration:

http://quelvint.co.uk
https://www.fendro.studio
https://www.zuplo.io (Client's Favorite)
https://www.merigoldcrafts.com
https://craftwimble.com
https://www.dravinsultonmask.com/us/home/

Thank you for taking the time to consider designing a website for us. We are web developers based in Stockton, CA, USA. Most of our projects go through the same process. Understanding this process may help you win a project with us. We custom-code all of our websites in-house. We don’t have any requirements as to what tools you use for your design, but we prefer Figma files. For any design that we label as four-stars, we send it to the client for review. The client picks the final design they want us to use. Once we complete this process, we will continue to show additional clients all the four-star sites and purchase them later. Your designs will have multiple chances to sell. For better chances of success, we ask that you follow these guidelines.

IMAGES:
If you use any images or icons in the design, we ask that you have a link to the asset so we can purchase the image/icon. Most of the designs we submit do not have the customer’s images on them unless they have some great images. Be creative; show us the feeling you are trying to portray with your image choices. Use any royalty-free site you choose. We subscribe to Tessaly and mainly use their images, but we can purchase images outside of Tessaly. PLEASE NOTE: we will not submit designs to clients with watermarks on the images.

FONTS:
We ask that you identify the fonts used in the design. This can be done in a message if you want. We typically use Brindle Fonts and Tessaly Fonts.

CONTENT:
We're always open to different content and ideas. We often submit designs with stock images so the client can see our vision. We typically take pictures after the website launch to use their images with our vision. Lorem Ipsum is fine for paragraphs, but we ask that you write the headers in correct English. We want to be able to show the vision and identify the sections of the website.

INSPIRATION:
We typically add a couple of links in the brief of websites we like to help you get started in your design.

REVISIONS:
We do not often ask for revisions of the designs unless we see something in the design that may not appeal to the client. If there are slight changes that we want to make, we do that in the development process.

FEEDBACK:
We rarely give feedback on designs during the design process. We are working on many website projects and do not have the time to provide feedback. We usually respond if your request is well thought out and asks specific questions, but a note asking “feedback, please” usually goes unanswered.

```html
<!DOCTYPE html>
<html lang="en">
<head>
<meta charset="utf-8">
<title>Velmora Creative</title>
<link rel="stylesheet" href="https://fonts.googleapis.com/css2?family=Inter+Tight:wght@300;400;500&family=Inter:wght@300;400;500&display=swap">
<style>
:root{
  --brown:#8a4b3f;
  --gold:#d9a94e;
  --ink:#221e1f;
  --paper:#f7f6f6;
  --white:#ffffff;
  --grey:#6d6868;
  --footer:#7a7878;
  --line:#cfcaca;
  --blush:#fbf1ee;
}
*{margin:0;padding:0;box-sizing:border-box}
html,body{width:1200px;height:4425px;overflow:hidden}
body{position:relative;background:var(--white);font-family:"Inter",sans-serif;color:var(--ink)}
.display{font-family:"Inter Tight",sans-serif;font-weight:300}
section,header,footer{position:absolute;left:0;width:1200px}
.abs{position:absolute}

.site-header{top:0;height:92px;background:var(--white)}
.brand{left:94px;top:24px;display:flex;align-items:center;gap:10px;color:var(--brown)}
.brand-dot{width:42px;height:42px;border-radius:50%;border:3px solid var(--brown)}
.brand-name{font-family:"Inter Tight",sans-serif;font-size:25px;letter-spacing:2px;line-height:1}
.brand-name small{display:block;font-size:14px;letter-spacing:3px;color:var(--gold);margin-top:2px}
.menu{left:1070px;top:36px;width:32px}
.menu span{display:block;height:2px;background:var(--brown);margin-bottom:7px}

.hero{top:92px;height:658px;background:var(--paper)}
.hero-title{left:94px;top:118px;font-size:92px;line-height:113px;color:var(--brown);letter-spacing:-1px}
.hero-copy{left:94px;top:484px;width:720px;font-size:18px;line-height:28px;color:var(--grey);font-weight:300}
.discover{left:943px;top:532px;display:flex;align-items:center;gap:10px;font-size:14px;letter-spacing:1.5px;color:var(--grey)}
.mouse{width:18px;height:28px;border:2px solid var(--grey);border-radius:9px;position:relative}
.mouse::after{content:"";position:absolute;left:6px;top:5px;width:2px;height:7px;background:var(--grey)}

.badge{width:200px;height:200px}

.tag{display:inline-block;border:1.5px solid var(--line);border-radius:20px;padding:5px 14px;font-size:14px;letter-spacing:1px;color:var(--grey);font-weight:500}

.about{top:750px;height:630px}
.about .tag{left:94px;top:74px}
.about-title{left:407px;top:58px;width:710px;font-size:50px;line-height:66px;color:var(--ink);letter-spacing:-0.5px}
.about-col{top:345px;width:235px;font-size:14.5px;line-height:25px;color:var(--ink);font-weight:300}
.about-col.a{left:407px}
.about-col.b{left:740px;width:350px}
.btn-gold{left:407px;top:525px;height:46px;width:213px;border-radius:23px;background:var(--gold);color:var(--white);display:flex;align-items:center;justify-content:center;gap:12px;font-size:14px;letter-spacing:1px}

.services{top:1380px;height:957px;background:var(--ink);color:var(--white)}
.services .tag{left:96px;top:86px;border-color:var(--white);color:var(--white);padding:4px 12px}
.services-intro{left:96px;top:145px;width:900px;font-family:"Inter Tight",sans-serif;font-size:24px;line-height:36px;font-weight:300}
.service-list{left:96px;top:293px;width:1011px;list-style:none}
.service-row{height:147px;border-top:1.5px solid #5b5556;display:flex;align-items:center;position:relative}
.service-num{width:44px;height:26px;border:1.5px solid var(--gold);border-radius:13px;color:var(--gold);font-size:14px;display:flex;align-items:center;justify-content:center;margin-right:36px;margin-top:-10px}
.service-name{font-family:"Inter Tight",sans-serif;font-size:42px;letter-spacing:-0.5px;font-weight:400}
.service-go{position:absolute;right:0;width:80px;height:80px;border-radius:50%;background:var(--blush);display:flex;align-items:center;justify-content:center}

.projects{top:2337px;height:1495px}
.projects .tag{left:94px;top:96px}
.projects-title{left:440px;top:78px;font-size:49px;line-height:66px;color:var(--ink);letter-spacing:-0.5px}
.card{width:493px}
.card-media{width:493px;height:297px}
.card-title{font-size:36px;margin-top:26px;color:var(--ink);font-weight:400}
.card-copy{font-size:14.5px;line-height:25px;color:var(--grey);font-weight:300;margin-top:12px;width:480px}
.chips{display:flex;gap:8px;margin-top:14px}
.chip{background:#ececec;border-radius:14px;padding:5px 12px;font-size:13px;letter-spacing:1px;color:var(--grey)}
.btn-outline{left:464px;top:1392px;width:219px;height:46px;border:1.5px solid var(--ink);border-radius:23px;display:flex;align-items:center;justify-content:center;gap:12px;font-size:14px;letter-spacing:1px}

.site-footer{top:3832px;height:593px;background:var(--footer);color:var(--white)}
.cta-title{left:68px;top:90px;font-size:130px;line-height:135px;letter-spacing:-3px;font-weight:400}
.footer-rule{left:68px;top:430px;width:1064px;height:1.5px;background:#a7a3a3}
.footer-nav{left:68px;top:472px;display:flex;gap:36px;font-size:14px}
.socials{left:880px;top:472px;display:flex;gap:16px;font-size:13px}
.legal{top:530px;font-size:13px}
</style>
</head>
<body>

<header class="site-header">
  <div class="brand abs"><span class="brand-dot"></span><span class="brand-name">VELMORA<small>CREATIVE</small></span></div>
  <div class="menu abs"><span></span><span></span><span></span></div>
</header>

<section class="hero">
  <h1 class="hero-title display abs">Designing your<br>tomorrow,<br>today</h1>
  <svg class="badge abs" style="left:906px;top:191px" viewBox="0 0 200 200" aria-label="Get in touch">
    <defs><path id="ring1" d="M100,100 m-72,0 a72,72 0 1,1 144,0 a72,72 0 1,1 -144,0"/></defs>
    <circle cx="100" cy="100" r="100" fill="#d9a94e"/>
    <text font-family="Inter,sans-serif" font-size="14" fill="#ffffff"><textPath href="#ring1" textLength="448" lengthAdjust="spacing">GET IN TOUCH · GET IN TOUCH · </textPath></text>
    <path d="M86 114 L114 86 M96 86 H114 V104" stroke="#ffffff" stroke-width="3" fill="none"/>
  </svg>
  <p class="hero-copy abs">We are a team of branding experts, marketing strategists, designers, and growth programmers. We use the strength of human psychology and our understanding of digital landscapes to help businesses attract customers.</p>
  <div class="discover abs">DISCOVER MORE <span class="mouse"></span></div>
</section>

<section class="about">
  <span class="tag abs">ABOUT US</span>
  <h2 class="about-title display abs">We have put together a special combination of strategy, marketing, design, and digital expertise.</h2>
  <p class="about-col a abs">Companies and organizations have no choice but to achieve perfection in a world of algorithms, artificial intelligence, and word-of-mouth.</p>
  <p class="about-col b abs">Velmora has assembled a group of strategists, designers, branding experts, business model specialists, and service designers. We assist our clients in excelling in their fields, or even more powerful.</p>
  <a class="btn-gold abs">SCHEDULE A CALL
    <svg width="14" height="14" viewBox="0 0 14 14"><path d="M2 12 L12 2 M5 2 H12 V9" stroke="#fff" stroke-width="1.5" fill="none"/></svg></a>
</section>

<section class="services">
  <span class="tag abs">OUR SERVICE</span>
  <p class="services-intro abs">As a 360-degree agency, we provide a variety of services. Our devoted team is made up of experts in a variety of disciplines, including digital advertising, design...</p>
  <ul class="service-list abs">
    <li class="service-row"><span class="service-num">01</span><span class="service-name">BRANDING &amp; STRATEGY</span><span class="service-go"><svg width="26" height="26" viewBox="0 0 26 26"><path d="M4 22 L22 4 M9 4 H22 V17" stroke="#221e1f" stroke-width="2" fill="none"/></svg></span></li>
    <li class="service-row"><span class="service-num">02</span><span class="service-name">LOGO DESIGN</span><span class="service-go"><svg width="26" height="26" viewBox="0 0 26 26"><path d="M4 22 L22 4 M9 4 H22 V17" stroke="#221e1f" stroke-width="2" fill="none"/></svg></span></li>
    <li class="service-row"><span class="service-num">03</span><span class="service-name">PACKAGING</span><span class="service-go"><svg width="26" height="26" viewBox="0 0 26 26"><path d="M4 22 L22 4 M9 4 H22 V17" stroke="#221e1f" stroke-width="2" fill="none"/></svg></span></li>
    <li class="service-row"><span class="service-num">04</span><span class="service-name">MARKETING COLLATERAL</span><span class="service-go"><svg width="26" height="26" viewBox="0 0 26 26"><path d="M4 22 L22 4 M9 4 H22 V17" stroke="#221e1f" stroke-width="2" fill="none"/></svg></span></li>
  </ul>
</section>

<section class="projects">
  <span class="tag abs">OUR PROJECTS</span>
  <h2 class="projects-title display abs">Take a look at our most<br>successful projects</h2>

  <article class="card abs" style="left:94px;top:293px">
    <div class="card-media" role="img" aria-label="Open type specimen book floating on a blue backdrop" style="background:linear-gradient(135deg,#4a63e0,#6f82ea)"></div>
    <h3 class="card-title display">Pelanduk</h3>
    <p class="card-copy">Increasing conversions by twofold on a new lorem ipsum site childcare website</p>
    <div class="chips"><span class="chip">MARKETING PLAN</span><span class="chip">BRANDING</span><span class="chip">WEBSITE</span></div>
  </article>

  <article class="card abs" style="left:613px;top:293px">
    <div class="card-media" role="img" aria-label="Hand sketching with a technical pen on paper" style="background:linear-gradient(135deg,#8f8a86,#e6e4e2)"></div>
    <h3 class="card-title display">Tarvex Bank</h3>
    <p class="card-copy">A new brand to carry out an ambitious marketing plan in the banking and fintech markets</p>
    <div class="chips"><span class="chip">BRANDING</span></div>
  </article>

  <article class="card abs" style="left:94px;top:825px">
    <div class="card-media" role="img" aria-label="Team gathered around a table in a bright studio" style="background:linear-gradient(135deg,#5e4a3c,#c9b9a6)"></div>
    <h3 class="card-title display">Mirelo</h3>
    <p class="card-copy">Creating a strong branding and viral campaign for a new online date mobile app</p>
    <div class="chips"><span class="chip">BRANDING</span><span class="chip">WEBSITE</span></div>
  </article>

  <article class="card abs" style="left:613px;top:825px">
    <div class="card-media" role="img" aria-label="Designer pinning prints to a white tiled wall" style="background:linear-gradient(135deg,#d8d8d8,#f3f3f3)"></div>
    <h3 class="card-title display">Lumaya</h3>
    <p class="card-copy">Becoming the market leader for beauty product through personalized marketing</p>
    <div class="chips"><span class="chip">BRANDING</span><span class="chip">PROGRAMMATIC ADVERTISING</span></div>
  </article>

  <a class="btn-outline abs">VIEW ALL PROJECT
    <svg width="14" height="14" viewBox="0 0 14 14"><path d="M2 12 L12 2 M5 2 H12 V9" stroke="#221e1f" stroke-width="1.5" fill="none"/></svg></a>
</section>

<footer class="site-footer">
  <h2 class="cta-title display abs">Let’s work<br>together</h2>
  <svg class="badge abs" style="left:862px;top:133px" viewBox="0 0 200 200" aria-label="Get in touch">
    <defs><path id="ring2" d="M100,100 m-72,0 a72,72 0 1,1 144,0 a72,72 0 1,1 -144,0"/></defs>
    <circle cx="100" cy="100" r="100" fill="#ffffff"/>
    <text font-family="Inter,sans-serif" font-size="14" fill="#8a4b3f"><textPath href="#ring2" textLength="448" lengthAdjust="spacing">GET IN TOUCH · GET IN TOUCH · </textPath></text>
    <path d="M86 114 L114 86 M96 86 H114 V104" stroke="#8a4b3f" stroke-width="3" fill="none"/>
  </svg>
  <div class="footer-rule abs"></div>
  <nav class="footer-nav abs"><span>About</span><span>Services</span><span>Projects</span><span>Blogs</span><span>Contact</span></nav>
  <div class="socials abs"><span>Nookbase</span><span>Quipster</span><span>Snapvale</span><span>Workloom</span></div>
  <p class="legal abs" style="left:68px">© 2024 Velmora. All rights reserved</p>
  <p class="legal abs" style="left:385px">Privacy Policy</p>
  <p class="legal abs" style="left:955px">Velmora - Creative Studio</p>
</footer>

</body>
</html>
```